Vantrell Law Letterhead

We need a new letterhead design for a Law Firm. The address for the law firm is 4817 Larkspur Boulevard, Suite 250, Houston, Texas 77342. Phone Number: 832-619-3057; Fax Number: 832-407-1694. The logo is uploaded to the project.

```html
<!DOCTYPE html>
<html lang="en">
<head>
<meta charset="utf-8">
<title>Vantrell Law Letterhead</title>
<link href="https://fonts.googleapis.com/css2?family=Quicksand:wght@500;600&display=swap" rel="stylesheet">
<style>
  :root {
    --backdrop: #c6c6c6;
    --paper: #ffffff;
    --navy: #14284b;
    --blue: #1f3868;
    --crimson: #76020d;
    --slate: #939393;
    --ink: #222222;
  }
  * { margin: 0; padding: 0; box-sizing: border-box; }
  html, body {
    width: 1200px; height: 1200px; overflow: hidden;
    background: var(--backdrop);
  }
  .letterhead {
    position: absolute; left: 200px; top: 82px;
    width: 800px; height: 1035px;
    background: var(--paper);
    overflow: hidden;
    font-family: "Quicksand", sans-serif;
    color: var(--ink);
  }
  .header-band {
    position: absolute; left: 0; top: 57px;
    width: 430px; height: 62px;
    background: var(--navy);
  }
  .brand {
    position: absolute; left: 452px; top: 40px;
    display: flex; align-items: center; gap: 16px;
  }
  .brand-square {
    width: 62px; height: 62px;
    background: var(--navy);
  }
  .brand-name {
    font-size: 40px; font-weight: 600;
    color: var(--navy); letter-spacing: 1px;
    white-space: nowrap;
  }
  .contact {
    position: absolute; left: 160px; top: 168px;
    font-size: 15px; font-weight: 500; line-height: 23px;
  }
  .signoff {
    position: absolute; left: 400px; top: 800px;
    font-size: 15px; font-weight: 500; line-height: 23px;
  }
  .signoff .signature { margin-top: 30px; padding-left: 28px; }
  .signoff .signer { padding-left: 28px; }
  .footer-shapes {
    position: absolute; left: 0; bottom: 0;
    width: 800px; height: 300px;
  }
</style>
</head>
<body>
  <main class="letterhead">
    <div class="header-band"></div>
    <div class="brand">
      <div class="brand-square"></div>
      <div class="brand-name">Vantrell Law</div>
    </div>

    <address class="contact" style="font-style:normal">
      4817 Larkspur Boulevard, Suite 250<br>
      Houston, Texas 77342<br>
      Phone : 832-619-3057<br>
      Fax : 832-407-1694
    </address>

    <div class="signoff">
      <p>Sincerely,</p>
      <p class="signature">( signature )</p>
      <p class="signer">Name</p>
    </div>

    <svg class="footer-shapes" viewBox="0 0 800 300" aria-hidden="true">
      <polygon points="630,20 800,26 800,300 630,300" fill="var(--slate)"/>
      <polygon points="320,250 432,256 432,300 320,300" fill="var(--blue)"/>
      <polygon points="446,178 600,186 600,300 446,300" fill="var(--navy)"/>
      <polygon points="532,58 800,68 800,300 540,300" fill="var(--crimson)"/>
    </svg>
  </main>
</body>
</html>
```